Book cover for the book The Copper Lantern Beneath Harrow Lake

This is a 6x9 paperback book titled The Copper Lantern Beneath Harrow Lake: Field Notes on Tidal Rhythms from Sailors and Keepers Along the Northern Coast. It will be a cover full of love, reunion, and warmth. No ghosts, cemeteries, and so on. I'm open to any creative design. Might include someone rising in spirit from a sick bed to the welcoming arms of loved ones. Or someone being greeted by family in a scene of enchanting beauty that is the life after this life. The world of the life after this life is just like earth, except more beautiful, with colors we can't imagine, large flowers, opulent buildings, and people all young wearing robes of varying colors. No religious symbols. No sun, moon, or stars.

Font styles to use
Serif

Requirements
Should not have
• Cemeteries, ghosts, anything ghoulish and spooky

```html
<!DOCTYPE html>
<html lang="en">
<head>
<meta charset="UTF-8">
<title>The Copper Lantern Beneath Harrow Lake — Cover</title>
<link rel="stylesheet" href="https://fonts.googleapis.com/css2?family=Urbanist:ital,wght@0,300;0,400;1,300;1,400&display=swap">
<style>
  :root {
    --backdrop: #e4e8ea;
    --cover-black: #050406;
    --ink-white: #ffffff;
    --art-violet: #3a2a6e;
    --art-indigo: #1c1840;
    --art-blue: #4a4fa8;
    --art-copper: #d9785a;
    --art-rose: #a83a4a;
  }
  * { margin: 0; padding: 0; box-sizing: border-box; }
  html, body {
    width: 1200px;
    height: 675px;
    overflow: hidden;
    background: var(--backdrop);
  }
  .stage {
    width: 1200px;
    height: 675px;
    display: flex;
    justify-content: center;
    align-items: center;
  }
  .book-cover {
    position: relative;
    width: 450px;
    height: 675px;
    background: var(--cover-black);
    color: var(--ink-white);
    font-family: "Urbanist", sans-serif;
    text-align: center;
    overflow: hidden;
  }
  .title-block {
    position: absolute;
    top: 30px;
    left: 0;
    right: 0;
  }
  .title {
    font-weight: 300;
    font-size: 58px;
    line-height: 50px;
    letter-spacing: 0.5px;
    text-transform: uppercase;
  }
  .title span { display: block; }
  .title-tagline {
    margin-top: 4px;
    font-weight: 300;
    font-style: italic;
    font-size: 30px;
    line-height: 34px;
  }
  .cover-art {
    position: absolute;
    top: 224px;
    left: 0;
    width: 450px;
    height: 301px;
    background:
      radial-gradient(ellipse 30% 35% at 62% 30%, rgba(217,120,90,0.85), transparent 70%),
      radial-gradient(ellipse 25% 25% at 45% 50%, rgba(168,58,74,0.7), transparent 70%),
      radial-gradient(ellipse 45% 50% at 20% 55%, rgba(74,79,168,0.8), transparent 75%),
      radial-gradient(ellipse 40% 40% at 85% 70%, rgba(58,42,110,0.9), transparent 75%),
      linear-gradient(160deg, var(--art-violet), var(--art-indigo));
  }
  .subtitle {
    position: absolute;
    top: 536px;
    left: 0;
    right: 0;
    font-weight: 300;
    font-style: italic;
    font-size: 16.5px;
    line-height: 21px;
  }
  .author-name {
    position: absolute;
    top: 607px;
    left: 0;
    right: 0;
    font-weight: 300;
    font-size: 22px;
    letter-spacing: 0.5px;
  }
</style>
</head>
<body>
  <main class="stage">
    <article class="book-cover">
      <header class="title-block">
        <h1 class="title"><span>The</span><span>Copper</span><span>Lantern</span></h1>
        <p class="title-tagline">beneath harrow lake</p>
      </header>
      <div class="cover-art" role="img" aria-label="Close-up photograph of gentle hands touching, lit in violet and warm copper tones"></div>
      <p class="subtitle">Field Notes on Tidal Rhythms from Sailors<br>and Keepers Along the Northern Coast</p>
      <p class="author-name">AUTHOR NAME</p>
    </article>
  </main>
</body>
</html>
```